Website/Logo redesign: FieldKinship.com

We need a web design for a sports social network.
We have already built the web-site but are unhappy with the current design.
We like colours that evoke outdoors, eg sky blue and grass green.
Please see how it currently looks:
http://www.fieldkinship.example/4b1a9c3e7d2f5a8b0c6e1f3a9d7b2c5e/
We are happy for everything to change, including logo, icons etc or for you to keep anything you think will work with your new design.
Reason: We have not yet found the design we are happy with so will be providing more feedback and extending the deadine.
We have increased the budget and also agreed to pay a second place award.
I will be giving existing and any new designs feedback daily.
Target Market(s)
Our target audience are mainly young sports players, but also older ones too.
Industry/Entity Type
Social
Look and feel

```html
<!DOCTYPE html>
<html lang="en">
<head>
<meta charset="utf-8">
<title>Field Kinship – Headline</title>
<link href="https://fonts.googleapis.com/css2?family=Ubuntu:wght@400;500&family=Open+Sans:wght@400;600&family=PT+Serif:wght@700&display=swap" rel="stylesheet">
<style>
:root{
  --grass:#6aae25;--grass-dark:#4f8d17;--grass-top:#5d9d1d;--grass-light:#86c63a;
  --ink:#2d2d2d;--muted:#666;--team:#4a8a12;--rival:#e0701a;
  --sky:#e8f3f8;--sky-head:#c5e2ef;--sky-ink:#2a6d8e;--line:#dcdcdc;--panel:#fff;--page:#f5f5f5;
}
*{box-sizing:border-box;margin:0;padding:0}
html,body{width:913px;height:1200px;overflow:hidden}
body{background:var(--page);font-family:"Ubuntu",sans-serif;color:var(--ink);position:relative}
.topbar{position:absolute;left:0;top:0;width:913px;height:28px;background:var(--grass-top);color:#fff;font-size:13px;text-align:right;padding:7px 22px 0 0}
.header{position:absolute;left:0;top:28px;width:913px;height:118px;background:linear-gradient(#7ebf31,#64a620);border-bottom:3px solid #9dd04f}
.brand{position:absolute;left:26px;top:48px;display:flex;align-items:center;gap:8px;color:#fff;font-size:24px;font-weight:500}
.brand .dot{width:14px;height:14px;border-radius:50%;background:#fff}
.nav{position:absolute;right:0;top:0;display:flex;height:118px}
.nav a{display:flex;flex-direction:column;align-items:center;justify-content:flex-start;padding-top:30px;color:#fff;text-decoration:none;font-size:15px;border-left:1px solid rgba(0,0,0,.12)}
.nav a svg{height:32px;margin-bottom:10px}
.nav a.active{background:linear-gradient(#8ccd44,#78b933);color:#3f7a0f}
.col{position:absolute;top:163px;height:987px;background:var(--panel);border:1px solid #e3e3e3;border-radius:3px}
.col-left{left:14px;width:222px}
.col-mid{left:241px;width:434px}
.col-right{left:678px;width:223px;background:var(--sky);border-color:#d3e4ec}
.profile{margin:3px 4px;height:178px;border:1px solid #e6e6e6;border-radius:6px;background:#fafafa;position:relative}
.avatar{background:linear-gradient(#c9a88a,#8a6a52);border-radius:2px}
.profile .avatar{position:absolute;left:16px;top:16px;width:71px;height:69px}
.profile .name{position:absolute;left:105px;top:23px;font-size:15px}
.profile .edit{position:absolute;left:101px;top:47px;background:#555;color:#fff;font-size:11px;border-radius:10px;padding:3px 17px}
.stats{position:absolute;top:106px;left:0;right:0;display:flex;justify-content:space-around;padding:0 4px}
.stat{text-align:center;font-size:11px;color:#555}
.stat b{display:flex;align-items:center;justify-content:center;width:37px;height:37px;border-radius:50%;background:var(--grass-dark);color:#fff;font-weight:400;font-size:15px;margin:0 auto 6px;border:2px solid #d9ecc2}
.create{margin:10px 4px 0;height:40px;border:1px solid #e0e0e0;background:linear-gradient(#fff,#f0f0f0);display:flex;align-items:center;gap:10px;padding-left:12px;font-size:13px}
.create i{width:22px;height:22px;border-radius:50%;background:#111;color:#fff;font-style:normal;display:flex;align-items:center;justify-content:center;font-size:16px}
.teams{list-style:none;margin:28px 0 0 21px}
.teams li{height:31px;display:flex;align-items:center;padding-left:21px;font-size:12px;color:var(--team);border-bottom:1px solid #9ccb6a;margin-left:12px}
.teams li.all{background:var(--grass-dark);color:#fff;font-size:14px;height:32px;margin:0 0 6px;padding-left:38px;border:0}
.quote{padding:28px 16px 0}
.quote h3{font-weight:500;font-size:16px;margin-bottom:10px}
.quote p{font-family:"Open Sans",sans-serif;font-size:10.5px;line-height:18px;color:#555}
.quote .author{display:inline-block;margin-top:8px;background:#eee;font-family:"PT Serif",serif;font-size:9.5px;padding:5px 12px;color:#444}
.sec-head{height:36px;background:linear-gradient(#fff,#efefef);border-bottom:1px solid #d5d5d5;font-size:14px;font-weight:500;padding:14px 15px 0;color:#333}
.fixture{display:flex;gap:13px;padding:14px 30px;height:72px;font-size:12px}
.ball{width:40px;height:40px;border:1px solid #ccc;flex:none;display:flex;align-items:center;justify-content:center;background:#fff}
.team{color:var(--team)}.rival{color:var(--rival)}
.fixture .when{margin-top:6px}
.comment{position:relative;height:66px;background:#f3f3f3;border-bottom:2px solid #fff;padding:8px 0 0 28px;display:flex;gap:12px}
.comment .avatar{width:53px;height:46px;flex:none}
.comment b{font-weight:400;font-size:12px;display:block;margin:4px 0 3px}
.comment p{font-family:"Open Sans",sans-serif;font-size:10px;line-height:15px;color:#555;width:280px}
.comment time{position:absolute;right:22px;bottom:10px;font-size:11px}
.reply{display:flex;margin:16px 25px 20px 31px;height:33px}
.reply input{flex:1;border:1px solid #ddd;border-right:0;border-radius:4px 0 0 4px;font-family:"Open Sans",sans-serif;font-style:italic;font-size:11px;padding-left:12px;color:#999}
.reply button{width:94px;background:linear-gradient(#79b832,#5b9a1c);color:#fff;border:0;border-radius:0 4px 4px 0;font-family:inherit;font-size:15px}
.result{position:relative;height:125px;border-bottom:1px solid #ddd;margin:0 5px 0 8px;padding:12px 16px;display:flex;gap:18px;font-size:12px}
.score{position:absolute;left:103px;top:62px;display:flex;align-items:center;gap:6px;font-size:17px;color:#444}
.score span{width:37px;height:37px;border-radius:50%;background:#ddd;display:flex;align-items:center;justify-content:center}
.tools{position:absolute;right:22px;bottom:-12px;display:flex;gap:6px}
.tools span{height:24px;border:1px solid #aaa;border-radius:12px;background:#f4f4f4;padding:0 10px;display:flex;align-items:center;gap:4px}
.feed-gap{height:30px}
.invite{position:relative;display:flex;gap:16px;padding:18px 17px 0 18px;height:118px;border-bottom:1px solid #e2e2e2;font-size:12px;line-height:19px}
.invite .avatar{width:53px;height:45px;flex:none}
.invite small{color:#777;font-size:11px}
.rsvp{display:flex;align-items:center;gap:7px;margin-top:7px}
.rsvp i{width:28px;height:28px;border-radius:50%;display:flex;align-items:center;justify-content:center;margin-left:2px}
.rsvp .yes{background:#7ac52c}.rsvp .no{background:#5c6659}
.invite time{position:absolute;right:18px;bottom:18px;font-size:12px;color:#555}
.side-head{margin:1px 1px 0;height:40px;background:linear-gradient(#d4ebf5,#bcdcea);color:var(--sky-ink);font-size:14px;font-weight:500;padding:15px 14px 0}
.upcoming{padding:14px 0 0 20px}
.match{display:flex;gap:16px;font-size:12px;line-height:19px;margin-bottom:18px}
.crests{display:flex;flex-direction:column;gap:10px;padding-top:4px}
.crest{width:34px;height:34px;border-radius:50%;background:#fff;border:2px solid #e2e2e2;display:flex;align-items:center;justify-content:center}
.crest::after{content:"";width:18px;height:20px;border-radius:3px 3px 9px 9px;background:#d9443c}
.league{margin:17px 7px 0;background:#fff;border:1px solid #d5e4ea;border-radius:4px;padding:8px 8px}
.league table{width:100%;border-collapse:collapse;font-size:12px;color:var(--sky-ink)}
.league td{height:31px;border-bottom:1px dashed #a9c7d4}
.league tr:last-child td{border:0}
.league td:first-child{width:28px;padding-left:8px;font-size:14px}
.league td.num{text-align:center;width:42px;font-size:14px;color:#4c9bc0}
</style>
</head>
<body>
<div class="topbar">Sign Out</div>
<header class="header">
  <div class="brand"><span class="dot"></span>Field Kinship</div>
  <nav class="nav">
    <a class="active" href="#" style="width:67px"><svg viewBox="0 0 34 32" width="34"><rect x="1" y="1" width="32" height="22" rx="2" fill="#4f8d17"/><path d="M8 23l-2 8 9-8z" fill="#4f8d17"/><path d="M11 12q6 6 12 0" stroke="#9dd04f" stroke-width="2" fill="none"/></svg>Headline</a>
    <a href="#" style="width:85px"><svg viewBox="0 0 32 32" width="32"><path d="M15 3a13 13 0 1 0 13 13H15z" fill="#fff"/><path d="M18 0v13h13A13 13 0 0 0 18 0z" fill="#fff"/></svg>My Stats</a>
    <a href="#" style="width:78px"><svg viewBox="0 0 22 32" width="22"><path d="M11 1q10 14 10 20a10 10 0 0 1-20 0q0-6 10-20z" fill="#fff"/><path d="M11 12q5 7 5 10a5 5 0 0 1-10 0q0-3 5-10z" fill="#6aae25"/></svg>Chllngrs</a>
    <a href="#" style="width:77px"><svg viewBox="0 0 32 32" width="32"><rect x="1" y="4" width="30" height="27" rx="3" fill="#fff"/><rect x="4" y="11" width="24" height="17" fill="#6aae25"/><g fill="#fff"><rect x="6" y="13" width="4" height="3"/><rect x="12" y="13" width="4" height="3"/><rect x="18" y="13" width="4" height="3"/><rect x="6" y="19" width="4" height="3"/><rect x="12" y="19" width="4" height="3"/><rect x="18" y="19" width="4" height="3"/><rect x="8" y="0" width="3" height="7"/><rect x="21" y="0" width="3" height="7"/></g></svg>Fixtures</a>
    <a href="#" style="width:64px"><svg viewBox="0 0 38 30" width="38"><circle cx="19" cy="8" r="6" fill="#fff"/><path d="M8 28q0-12 11-12t11 12z" fill="#fff"/><circle cx="8" cy="10" r="4" fill="#fff"/><circle cx="30" cy="10" r="4" fill="#fff"/><path d="M0 26q0-10 8-10l3 1q-5 4-5 9zM38 26q0-10-8-10l-3 1q5 4 5 9z" fill="#fff"/></svg>Team</a>
    <a href="#" style="width:73px"><svg viewBox="0 0 32 32" width="30"><path d="M16 1l4.6 10 10.4 1-8 7 2.5 11L16 24l-9.5 6L9 19 1 12l10.4-1z" fill="#fff"/></svg>Leagues</a>
    <a href="#" style="width:76px"><svg viewBox="0 0 32 32" width="30"><path d="M4 28L22 10M10 10L28 28" stroke="#fff" stroke-width="4" stroke-linecap="round"/><circle cx="25" cy="7" r="5" fill="none" stroke="#fff" stroke-width="3"/><circle cx="7" cy="7" r="4" fill="#fff"/></svg>Tools</a>
  </nav>
</header>

<aside class="col col-left">
  <div class="profile">
    <div class="avatar" role="img" aria-label="Profile photo of Tom Rendall"></div>
    <div class="name">Tom Rendall</div>
    <span class="edit">edit profile</span>
    <div class="stats">
      <div class="stat"><b>24</b>Played</div>
      <div class="stat"><b>3</b>Teams</div>
      <div class="stat"><b>7</b>Awards</div>
    </div>
  </div>
  <div class="create"><i>+</i>CREATE NEW FIXTURE</div>
  <ul class="teams">
    <li class="all">ALL TEAM</li>
    <li>FOOTBALL TEAM B</li>
    <li>GALATIANS HOUSE</li>
    <li>U15 RUGBY TEAM A</li>
  </ul>
  <div class="quote">
    <h3>Quote of the Day</h3>
    <p>Brightfield Webworks is a web service company, offering a wide range of services which range from designing and development, that is covering almost all the fields in the best possible way.</p>
    <span class="author">BY AUTHOR NAME</span>
  </div>
</aside>

<main class="col col-mid">
  <div class="sec-head">NEXT FIXTURE</div>
  <div class="fixture">
    <div class="ball"><svg viewBox="0 0 30 30" width="30"><circle cx="15" cy="15" r="13" fill="#fff" stroke="#222" stroke-width="2"/><path d="M15 10l5 3.5-2 6h-6l-2-6z" fill="#222"/></svg></div>
    <div><span class="team">U15 Football Team vs</span><span class="rival">Colossian House</span><div class="when">Sunday, 29th July, 1 PM</div></div>
  </div>
  <div class="comment"><div class="avatar" role="img" aria-label="Photo of Mr. Hartwell"></div><div><b>Mr. Hartwell</b><p>We act in accordance with the Industry certified processes to deliver the best to our clients all over the world.</p></div><time>2m ago</time></div>
  <div class="comment"><div class="avatar" role="img" aria-label="Photo of Alan Sorley"></div><div><b>Alan Sorley</b><p>We act in accordance with the Industry certified processes to deliver the best to our clients all over the world.</p></div><time>2m ago</time></div>
  <div class="comment"><div class="avatar" role="img" aria-label="Photo of Lena Warrick"></div><div><b>Lena Warrick</b><p>We act in accordance with the Industry certified processes to deliver the best to our clients all over the world.</p></div><time>2m ago</time></div>
  <form class="reply"><input value="Leave your Comment here.." readonly><button type="button">Submit</button></form>

  <div class="sec-head">LAST RESULT</div>
  <div class="result">
    <div class="ball"><svg viewBox="0 0 30 30" width="30"><circle cx="15" cy="15" r="13" fill="#fff" stroke="#222" stroke-width="2"/><path d="M15 10l5 3.5-2 6h-6l-2-6z" fill="#222"/></svg></div>
    <div><span class="team">Harbourton Danes</span> vs <span class="rival">Colossian House</span><div style="margin-top:6px">Friday, 29th July, 1 PM</div></div>
    <div class="score"><span>2</span>:<span>1</span></div>
    <div class="tools">
      <span><svg width="16" height="12" viewBox="0 0 16 12"><rect x="1" y="1" width="14" height="9" fill="none" stroke="#888"/><path d="M4 4h8M4 7h6" stroke="#888"/></svg></span>
      <span><svg width="16" height="14" viewBox="0 0 16 14"><rect x="1" y="2" width="14" height="11" fill="#333"/><path d="M3 6h10M3 9h10" stroke="#fff"/></svg><svg width="8" height="6" viewBox="0 0 8 6"><path d="M0 0h8L4 6z" fill="#333"/></svg></span>
    </div>
  </div>
  <div class="feed-gap"></div>
  <div class="sec-head">NEWS FEED</div>
  <div class="invite"><div class="avatar" role="img" aria-label="Photo of Mr. Hartwell"></div><div><span class="team">Mr. Hartwell</span> <small>Invites you to match</small><br><span class="team">Harbourton Danes</span> vs <span class="rival">Colossian House</span><br>Friday, 29th July, 1 PM<div class="rsvp">RSVP: <i class="yes"><svg width="14" height="12" viewBox="0 0 14 12"><path d="M1 6l4 4 8-9" stroke="#fff" stroke-width="2.5" fill="none"/></svg></i><i class="no"><svg width="11" height="11" viewBox="0 0 11 11"><path d="M1 1l9 9M10 1l-9 9" stroke="#fff" stroke-width="2.5"/></svg></i></div></div><time>1 hour ago</time></div>
  <div class="invite"><div class="avatar" role="img" aria-label="Photo of Mr. Kesby"></div><div><span class="team">Mr. Kesby</span> <small>Invites you to match</small><br><span class="team">Harbourton Danes</span> vs <span class="rival">Colossian House</span><br>Friday, 29th July, 1 PM<div class="rsvp">RSVP: <i class="yes"><svg width="14" height="12" viewBox="0 0 14 12"><path d="M1 6l4 4 8-9" stroke="#fff" stroke-width="2.5" fill="none"/></svg></i><i class="no"><svg width="11" height="11" viewBox="0 0 11 11"><path d="M1 1l9 9M10 1l-9 9" stroke="#fff" stroke-width="2.5"/></svg></i></div></div><time>4 hour ago</time></div>
  <div class="invite" style="border:0"><div class="avatar" role="img" aria-label="Photo of Jonah Belford"></div><div><span class="team">Jonah Belford</span> <small>Invites you to match</small><br><span class="team">Harbourton Danes</span> vs <span class="rival">Colossian House</span><br>Friday, 29th July, 1 PM<div class="rsvp">RSVP: <i class="yes"><svg width="14" height="12" viewBox="0 0 14 12"><path d="M1 6l4 4 8-9" stroke="#fff" stroke-width="2.5" fill="none"/></svg></i><i class="no"><svg width="11" height="11" viewBox="0 0 11 11"><path d="M1 1l9 9M10 1l-9 9" stroke="#fff" stroke-width="2.5"/></svg></i></div></div><time style="bottom:-10px">2 days ago</time></div>
</main>

<aside class="col col-right">
  <div class="side-head">UPCOMING FIXTURES</div>
  <div class="upcoming">
    <div class="match"><div class="crests"><span class="crest"></span><span class="crest"></span></div><div><span class="team">U15 Football Team</span> vs<br><span class="rival">Colossian House</span><br>29th July<br><span style="display:block;margin-top:6px">RVSP: Available</span></div></div>
    <div class="match" style="margin-top:24px"><div class="crests"><span class="crest"></span><span class="crest"></span></div><div><span class="team">U15 Football Team</span> vs<br><span class="rival">Colossian House</span><br>29th July<br><span style="display:block;margin-top:6px">RVSP: Available</span></div></div>
  </div>
  <div class="side-head" style="margin-top:14px">LEAGUE TABLE</div>
  <div class="league">
    <table>
      <tr><td>1</td><td>Colossians</td><td class="num">12</td><td class="num">36</td></tr>
      <tr><td>2</td><td>Phillippians</td><td class="num">12</td><td class="num">30</td></tr>
      <tr><td>3</td><td>Galatians</td><td class="num">11</td><td class="num">12</td></tr>
      <tr><td>4</td><td>Romans</td><td class="num">12</td><td class="num">4</td></tr>
      <tr><td>5</td><td>Corinthians</td><td class="num">11</td><td class="num">1</td></tr>
    </table>
  </div>
</aside>
</body>
</html>
```